I want both print and ebook covers

book title is "The Classroom MEETING HANDBOOK: Fresh Paths to Partner With Families For Student Growth. I want a dark Teal or Navy Background. Yellow and white letters. Distorted Picture of one teacher, two parents and one child around a table or desk. But no Martians! My name should include "Award Winning Author"

Target Market(s)

teachers and other educators--principals, school psychologists, speech therapists, etc.

Industry/Entity Type

schools

Font styles to use
Other font styles liked:
• I just need to see how it looks

Colors
0054AA
0677BA
7BADD7
CADEEF
E8F1F8
0094D4
00A9DD
6FCCEA
C7EBF8
E9F6FB
FFC000
F8CF3A
FAE287
FDF2CF
FEFAEE

Requirements
Must have
• Title top third of page big enough to be read when reduced greatly in size. Contrast so that it "pops'.
Nice to have
• Teacher, two parents and one child around a table/desk. My name should include 'Award winning author'

```html
<!DOCTYPE html>
<html lang="en">
<head>
<meta charset="utf-8">
<title>The Classroom Meeting Handbook – Cover</title>
<link href="https://fonts.googleapis.com/css2?family=Barlow+Condensed:wght@500;600;700&family=Montserrat:wght@700&display=swap" rel="stylesheet">
<style>
  :root {
    --stage: #f4f6f9;
    --navy-deep: #0a2748;
    --navy: #0d3663;
    --navy-soft: #12467c;
    --gold: #ffc000;
    --gold-soft: #f8cf3a;
    --white: #ffffff;
    --ice: #c7ebf8;
    --sky: #7badd7;
    --teal: #0677ba;
  }
  * { margin: 0; padding: 0; box-sizing: border-box; }
  html, body {
    width: 1200px; height: 675px; overflow: hidden;
    background: var(--stage);
  }
  .stage {
    width: 1200px; height: 675px;
    display: flex; align-items: center; justify-content: center;
  }
  .cover {
    width: 420px; height: 630px;
    background: linear-gradient(180deg, var(--navy-deep), var(--navy) 60%, var(--navy-deep));
    box-shadow: 0 10px 30px rgba(10, 39, 72, 0.3);
    display: flex; flex-direction: column; align-items: center;
    padding: 30px 0 26px;
    font-family: "Barlow Condensed", sans-serif;
  }
  .title {
    display: flex; flex-direction: column; align-items: center;
    text-transform: uppercase;
    font-weight: 700;
  }
  .title-lead {
    display: flex; align-items: center; gap: 10px;
    width: 370px;
    color: var(--gold);
    font-weight: 600; font-size: 38px; line-height: 1;
  }
  .title-lead::before, .title-lead::after {
    content: ""; flex: 1; height: 3px; background: var(--gold);
  }
  .title-main {
    color: var(--white);
    font-size: 96px; line-height: 0.9;
    letter-spacing: -1px;
  }
  .title-mid {
    color: var(--gold-soft);
    font-weight: 600; font-size: 44px; line-height: 1;
    margin-top: 4px;
  }
  .title-end {
    color: var(--gold);
    font-size: 94px; line-height: 0.92;
    letter-spacing: -1px;
  }
  .title-rule {
    width: 130px; height: 3px; background: var(--ice);
    margin: 12px 0;
  }
  .subtitle {
    color: var(--white);
    font-weight: 500; font-size: 23px; line-height: 1.15;
    text-align: center;
  }
  .scene {
    width: 100%; height: 150px; margin-top: 18px;
    background:
      radial-gradient(ellipse 40% 55% at 55% 55%, var(--teal), transparent 70%),
      radial-gradient(ellipse 12% 30% at 30% 60%, var(--gold-soft), transparent 70%),
      linear-gradient(180deg, var(--navy-soft), var(--navy));
  }
  .byline {
    margin-top: auto;
    text-align: center;
  }
  .byline-label {
    color: var(--gold);
    text-transform: uppercase;
    font-weight: 600; font-size: 19px; letter-spacing: 0.5px;
  }
  .byline-name {
    font-family: "Montserrat", sans-serif;
    color: var(--white);
    font-weight: 700; font-size: 30px; line-height: 1.1;
    margin-top: 2px;
  }
</style>
</head>
<body>
  <main class="stage">
    <article class="cover">
      <h1 class="title">
        <span class="title-lead">The</span>
        <span class="title-main">Classroom</span>
        <span class="title-mid">Meeting</span>
        <span class="title-end">Handbook</span>
      </h1>
      <div class="title-rule"></div>
      <p class="subtitle">Fresh Paths to Partner With Families<br>For Student Growth</p>
      <div class="scene" role="img" aria-label="Flat illustration of a teacher, two parents and a child seated around a desk in a school office beside a principal's door and a potted plant"></div>
      <footer class="byline">
        <p class="byline-label">Award Winning Author</p>
        <p class="byline-name">AUTHOR NAME</p>
      </footer>
    </article>
  </main>
</body>
</html>
```